Webdesign für Getränkelogistik & Full-Service-Partner bei Events
Zielgruppe
Getränkelogistiker und Full-Service-Partner bei Events
Zielgruppe: Getränke-EinzelHändler; Veranstalter von Events und privaten Feiern
Aufgabenstellung
- soll „Frische“ und „Moderne“ vermitteln, ohne eine Getränkeart in den Vordergrund zu rücken
- soll von den Farben her gut zum Logo passen (siehe Anlagen)
- Slider wäre wünschenswert
- Slogan 'Wir freuen uns auf Sie!'

```html
<!DOCTYPE html>
<html lang="de">
<head>
<meta charset="utf-8">
<title>Quellhof Getränke GmbH</title>
<link rel="stylesheet" href="https://fonts.googleapis.com/css2?family=Open+Sans:wght@400;600;700&family=Playfair+Display:wght@400;700&display=swap">
<style>
  :root {
    --green-dark: #1d5b4b;
    --green-text: #215f50;
    --yellow: #f6c100;
    --yellow-deep: #f4c20d;
    --yellow-light: #fbe35a;
    --text: #333333;
    --rule: #cfcfcf;
    --hero-dark: #05300a;
    --hero-mid: #0f5f18;
    --hero-light: #25a832;
    --ice: #e4ece4;
  }
  * { margin: 0; padding: 0; box-sizing: border-box; }
  html, body { width: 1146px; height: 1200px; overflow: hidden; background: #fff; }
  body { position: relative; font-family: "Open Sans", sans-serif; color: var(--text); }

  .brand {
    position: absolute; top: 28px; left: 0; width: 1146px;
    display: flex; justify-content: center; align-items: center; gap: 10px;
  }
  .brand-dot { width: 30px; height: 30px; border-radius: 50%; background: var(--yellow); }
  .brand-name { font-weight: 700; font-size: 24px; color: var(--green-dark); }

  .main-nav {
    position: absolute; left: 222px; top: 90px; width: 702px; height: 47px;
    border-top: 1px solid var(--rule); border-bottom: 1px solid var(--rule);
    display: flex; justify-content: center; align-items: center; gap: 28px;
    font-size: 11px; color: #444;
  }
  .main-nav .active { font-weight: 700; color: var(--green-dark); }

  .hero {
    position: absolute; left: 140px; top: 154px; width: 865px; height: 421px; overflow: hidden;
    background: linear-gradient(90deg, var(--hero-dark) 0%, #0a4510 30%, var(--hero-mid) 55%, #138a1f 100%);
  }
  .hero-photo {
    position: absolute; inset: 0;
    background:
      radial-gradient(ellipse 55% 28% at 78% 100%, rgba(228,236,228,0.95) 0%, rgba(200,225,200,0.6) 45%, rgba(40,150,50,0) 100%),
      radial-gradient(ellipse 45% 60% at 68% 40%, rgba(45,185,58,0.75) 0%, rgba(30,140,40,0.35) 50%, rgba(20,100,28,0) 100%);
  }
  .hero-slogan {
    position: absolute; left: 82px; top: 122px;
    font-family: "Playfair Display", serif; font-weight: 400; font-size: 38px; line-height: 44px; color: var(--yellow);
  }
  .slider-thumbs { position: absolute; left: 82px; top: 362px; display: flex; gap: 6px; }
  .slider-thumbs span { width: 42px; height: 42px; display: block; }
  .slider-thumbs .current { border: 2px solid var(--yellow); background: linear-gradient(135deg, #0a4a12, #2c9a36 70%, #cfe3cf); }
  .thumb-party { background: linear-gradient(135deg, #f6d0b8, #d4503a 60%, #a82a20); }
  .thumb-wine { background: linear-gradient(135deg, #f3cf96, #b0502a 55%, #5a1a10); }
  .thumb-drinks { background: linear-gradient(135deg, #cdeef8, #8fd06a 55%, #f2a536); }

  .hotline {
    position: absolute; left: 994px; top: 172px; width: 152px; height: 57px;
    background: var(--yellow); padding: 9px 0 0 11px;
  }
  .hotline-label { font-size: 11px; color: #3a3a2a; }
  .hotline-number { font-size: 19px; font-weight: 700; color: var(--green-dark); line-height: 24px; }

  .page-bottom {
    position: absolute; left: 139px; top: 900px; width: 867px; height: 300px;
    background: linear-gradient(180deg, #ffffff 0%, #eeeeee 22%, #dcdcdc 33%, var(--yellow-deep) 35%, #f8cf22 70%, var(--yellow-light) 100%);
  }

  .services { position: absolute; left: 222px; top: 645px; display: flex; gap: 17px; }
  .service { width: 163px; position: relative; }
  .service-label { font-size: 10.5px; font-weight: 700; color: var(--yellow); letter-spacing: 0.2px; }
  .service-rule { width: 30px; height: 1px; background: #bbb; margin: 10px 0 14px; }
  .service-title { font-family: "Playfair Display", serif; font-weight: 700; font-size: 23px; color: var(--green-text); line-height: 28px; margin-left: -1px; }
  .service-text { font-size: 10.5px; line-height: 16.6px; margin-top: 16px; color: #3a3a3a; }
  .service-photo { width: 162px; height: 111px; margin-top: 14px; }
  .photo-event { background: linear-gradient(180deg, #2a3fc0 0%, #6f88d8 35%, #d8dde8 65%, #f2f2f0 100%); }
  .photo-trucks { background: linear-gradient(180deg, #d6dbe0 0%, #c9c8a0 22%, #2a6a42 48%, #1f5634 72%, #7c7f7c 100%); }
  .photo-office { background: linear-gradient(135deg, #dfe3e1 0%, #b3bcb8 45%, #e9ebe9 100%); }
  .photo-crew { background: linear-gradient(180deg, #cfc33a 0%, #4a4e42 30%, #2e4a36 65%, #8c8c88 100%); }
  .read-more {
    display: block; text-align: right; margin-top: 16px; font-size: 11px; font-weight: 700;
    color: var(--green-dark); text-decoration: underline;
  }

  .site-footer { position: absolute; left: 222px; top: 1063px; width: 702px; font-size: 11px; color: #2a2a20; }
  .footer-col { position: absolute; top: 0; line-height: 21.5px; }
  .footer-address { left: 0; padding-left: 19px; }
  .footer-contact { left: 242px; padding-left: 23px; }
  .footer-links { left: 479px; list-style: none; }
  .footer-links li::before { content: "• "; }
  .footer-col svg { position: absolute; left: 0; }
  .footer-rule { position: absolute; left: 222px; top: 1160px; width: 702px; height: 1px; background: #5b5a3a; }
  .copyright { position: absolute; top: 1171px; left: 0; width: 1146px; text-align: center; font-size: 11px; color: #2a2a20; }
</style>
</head>
<body>
  <header class="brand">
    <span class="brand-dot"></span>
    <span class="brand-name">Quellhof Getränke</span>
  </header>

  <nav class="main-nav">
    <span class="active">Home</span>
    <span>Unternehmen</span>
    <span>Team</span>
    <span>Großhandel</span>
    <span>Rund um Ihr Event</span>
    <span>Karriere</span>
    <span>Kontakt</span>
  </nav>

  <section class="hero">
    <div class="hero-photo" role="img" aria-label="Zwei grüne Glasflaschen auf Eiswürfeln vor grünem Hintergrund"></div>
    <h1 class="hero-slogan">“Wir freuen uns<br>auf Sie!”</h1>
    <div class="slider-thumbs">
      <span class="current" role="img" aria-label="Vorschau: Flaschen auf Eis"></span>
      <span class="thumb-party" role="img" aria-label="Vorschau: Anstoßen auf einer Feier"></span>
      <span class="thumb-wine" role="img" aria-label="Vorschau: Weingläser"></span>
      <span class="thumb-drinks" role="img" aria-label="Vorschau: Erfrischungsgetränke mit Minze"></span>
    </div>
  </section>

  <aside class="hotline">
    <div class="hotline-label">Bestell-Hotline:</div>
    <div class="hotline-number">034512 40210</div>
  </aside>

  <div class="page-bottom" role="img" aria-label="Hintergrund: Bierschaum über goldgelbem Bier"></div>

  <main class="services">
    <article class="service">
      <div class="service-label">SERVICE 01</div>
      <div class="service-rule"></div>
      <h2 class="service-title">Für Ihr Event</h2>
      <p class="service-text">Dies ist ein Typoblindtext. An ihm kann man sehen, ob alle Buchstaben da sind und wie sie aussehen.</p>
      <div class="service-photo photo-event" role="img" aria-label="Festlich dekorierter Eventbereich mit Zelt"></div>
      <a class="read-more">weiterlesen</a>
    </article>
    <article class="service">
      <div class="service-label">SERVICE 02</div>
      <div class="service-rule"></div>
      <h2 class="service-title">Großhandel</h2>
      <p class="service-text">Dies ist ein Typoblindtext. An ihm kann man sehen, ob alle Buchstaben da sind und wie sie aussehen.</p>
      <div class="service-photo photo-trucks" role="img" aria-label="Grüne Lieferwagen der Flotte in einer Reihe"></div>
      <a class="read-more">weiterlesen</a>
    </article>
    <article class="service">
      <div class="service-label">SERVICE 03</div>
      <div class="service-rule"></div>
      <h2 class="service-title">Unternehmen</h2>
      <p class="service-text">Dies ist ein Typoblindtext. An ihm kann man sehen, ob alle Buchstaben da sind und wie sie aussehen.</p>
      <div class="service-photo photo-office" role="img" aria-label="Geschäftsführer im Bürogebäude am Geländer"></div>
      <a class="read-more">weiterlesen</a>
    </article>
    <article class="service">
      <div class="service-label">SERVICE 04</div>
      <div class="service-rule"></div>
      <h2 class="service-title">Team</h2>
      <p class="service-text">Dies ist ein Typoblindtext. An ihm kann man sehen, ob alle Buchstaben da sind und wie sie aussehen.</p>
      <div class="service-photo photo-crew" role="img" aria-label="Gruppenfoto des Teams vor der Lagerhalle"></div>
      <a class="read-more">weiterlesen</a>
    </article>
  </main>

  <footer class="site-footer">
    <div class="footer-col footer-address">
      <svg width="13" height="17" viewBox="0 0 13 17" style="top:-1px"><path d="M6.5 0C2.9 0 0 2.8 0 6.3 0 11 6.5 17 6.5 17S13 11 13 6.3C13 2.8 10.1 0 6.5 0Zm0 8.8a2.5 2.5 0 1 1 0-5 2.5 2.5 0 0 1 0 5Z" fill="#1d5b4b"/></svg>
      Quellhof Getränke GmbH<br>Am Brunnenweg 14<br>09471 Lindenau
    </div>
    <div class="footer-col footer-contact">
      <svg width="16" height="16" viewBox="0 0 24 24" style="top:0"><path d="M6.6 10.8a15.1 15.1 0 0 0 6.6 6.6l2.2-2.2c.3-.3.7-.4 1-.2 1.1.4 2.300.6 3.6.6.6 0 1 .4 1 1V20c0 .6-.4 1-1 1C10.6 21 3 13.4 3 4c0-.6.4-1 1-1h3.5c.6 0 1 .4 1 1 0 1.3.2 2.5.6 3.6.1.3 0 .7-.2 1l-2.3 2.2Z" fill="#1d5b4b"/></svg>
      <svg width="16" height="12" viewBox="0 0 16 12" style="top:48px"><rect width="16" height="12" rx="1" fill="#1d5b4b"/><path d="M1 1.5 8 7l7-5.5" stroke="#f6c100" stroke-width="1.3" fill="none"/></svg>
      Telefon: +49 34512 40210<br>Telefax: +49 34512 40211<br>info(at)quellhof-getraenke.de
    </div>
    <ul class="footer-col footer-links" style="top:-3px">
      <li>Downloads</li>
      <li>Kontakt</li>
      <li>Impressum/Datenschutz</li>
      <li>AGB</li>
    </ul>
  </footer>
  <div class="footer-rule"></div>
  <div class="copyright">© 2020 quellhof-getraenke.de</div>
</body>
</html>
```